Fleet Wrap - Wall Partitions Company

We are looking for a vehicle/fleet wrap design for Brightfold Panel Works, a company that sells and installs operable/folding wall partitions for commercial spaces. Our systems are used in offices, schools, hotels, conference centers, and other spaces that need flexible room configurations.

The goal of the wrap is to improve brand visibility and recognition while our vehicles are on the road and at job sites. We want the design to feel modern, professional, architectural, and memorable, while making it immediately clear what our company does.

The design should incorporate imagery, graphics, or architectural elements that communicate movable walls, folding partitions, and/or flexible spaces, along with our company colors (see logo attached). As well as display our logo/name, location, and phone number (obtained from our website - brightfoldpanels.example). We are open to creative concepts, but would prefer something clean and distinctive rather than overly busy.

The vehicle we want wrapped, is a KESTA Voyant 2400 (see link here - https://www.kestavans.example/kesta-voyant/specs.2400-cargo-van-high-roof-159-wb.html)

Key priorities:
- Strong brand visibility from a distance
- Contemporary, architectural look
- Clearly communicate that we sell and install folding/operable wall systems
- Easy-to-read company name and website
- Professional enough for commercial construction and corporate clients

```html
<!DOCTYPE html>
<html lang="en">
<head>
<meta charset="utf-8">
<title>Brightfold Panel Works – Fleet Wrap</title>
<link rel="stylesheet" href="https://fonts.googleapis.com/css2?family=Montserrat:ital,wght@0,500;0,600;0,700;0,800;1,500&display=swap">
<style>
  :root {
    --backdrop: #bfc3c4;
    --wrap-slate: #444b5a;
    --wrap-white: #f5f6f7;
    --wrap-blue: #1e9be8;
    --trim-black: #1f2022;
    --glass: #5d636c;
    --ink: #1d1f24;
    --label-white: #ffffff;
    --photo-light: #eef0f1;
    --photo-mid: #b9bec3;
  }
  html, body { margin: 0; padding: 0; overflow: hidden; background: var(--backdrop); }
  .canvas { width: 1200px; height: 1126px; display: block; }
  .slate { fill: var(--wrap-slate); }
  .white-field { fill: var(--wrap-white); }
  .blue-band { fill: var(--wrap-blue); }
  .trim { fill: var(--trim-black); }
  .glass { fill: var(--glass); }
  .tyre { fill: var(--trim-black); }
  .rim { fill: #9ba0a6; }
  .hub { fill: #3a3d42; }
  .panel-seam { stroke: #2b3038; stroke-width: 2; fill: none; opacity: .5; }
  .contact { font-family: "Montserrat", sans-serif; font-style: italic; font-weight: 500; font-size: 19px; fill: var(--label-white); }
  .brand-name { font-family: "Montserrat", sans-serif; font-weight: 600; font-size: 46px; fill: var(--label-white); letter-spacing: 1px; }
  .brand-square { fill: #f3b623; }
  .phone-line { font-family: "Montserrat", sans-serif; font-weight: 800; font-size: 44px; fill: var(--ink); }
  .since { font-family: "Montserrat", sans-serif; font-weight: 700; font-size: 29px; fill: var(--ink); }
  .web { font-family: "Montserrat", sans-serif; font-weight: 700; font-size: 25px; fill: var(--ink); }
  .icon-disc { fill: var(--label-white); }
  .icon-disc-dark { fill: var(--ink); }
  .icon-stroke { fill: none; stroke: var(--wrap-slate); stroke-width: 2; }
  .icon-stroke-light { fill: none; stroke: var(--label-white); stroke-width: 2; }
  .photo-ring { fill: none; stroke: #dfe2e4; stroke-width: 10; }
</style>
</head>
<body>
<svg class="canvas" viewBox="0 0 1988 1866" xmlns="http://www.w3.org/2000/svg">
  <defs>
    <clipPath id="van-body">
      <path d="M90 720 L95 620 Q110 560 200 520 L340 420 Q520 240 620 150 Q650 125 760 122 L1800 112 Q1840 115 1850 140 L1890 360 L1900 745 L100 775 Z"/>
    </clipPath>
    <radialGradient id="room-tone" cx="50%" cy="45%" r="60%">
      <stop offset="0" stop-color="var(--photo-light)"/>
      <stop offset="1" stop-color="var(--photo-mid)"/>
    </radialGradient>
    <g id="van-side">
      <g clip-path="url(#van-body)">
        <rect class="slate" x="60" y="90" width="1880" height="720"/>
        <path class="blue-band" d="M80 555 C300 505 620 525 900 528 C1200 530 1520 330 1910 300 L1910 820 L80 820 Z"/>
        <path class="white-field" d="M80 575 C300 525 620 548 900 548 C1200 548 1520 390 1910 345 L1910 820 L80 820 Z"/>
        <path class="panel-seam" d="M730 125 L735 740 M1135 118 L1140 740 M700 235 L1840 240"/>
        <path class="trim" d="M540 685 L1445 678 L1440 730 L545 740 Z"/>
        <path class="trim" d="M80 600 L200 580 L210 770 L80 775 Z"/>
        <path class="trim" d="M1860 600 L1900 600 L1900 750 L1860 752 Z"/>
      </g>
      <path class="glass" d="M420 380 L520 275 Q545 262 660 262 Q672 265 670 280 L660 450 Q655 465 640 466 L470 478 Q440 480 430 460 Z"/>
      <path class="trim" d="M330 480 Q330 400 390 380 L440 380 L450 490 Z"/>
      <path class="trim" d="M210 720 Q220 580 340 575 Q470 575 510 720 Z"/>
      <path class="trim" d="M1470 720 Q1490 590 1610 585 Q1740 590 1760 720 Z"/>
      <circle class="tyre" cx="340" cy="755" r="112"/>
      <circle class="rim" cx="340" cy="755" r="70"/>
      <circle class="hub" cx="340" cy="755" r="22"/>
      <circle class="tyre" cx="1620" cy="760" r="112"/>
      <circle class="rim" cx="1620" cy="760" r="70"/>
      <circle class="hub" cx="1620" cy="760" r="22"/>
    </g>
  </defs>

  <!-- Driver-side view -->
  <g class="van van--driver-side">
    <use href="#van-side"/>
    <circle class="icon-disc" cx="783" cy="178" r="16"/>
    <path class="icon-stroke" d="M783 188 C777 180 776 176 776 173 A7 7 0 0 1 790 173 C790 176 789 180 783 188 Z"/>
    <text class="contact" x="815" y="172">214 Alder Row</text>
    <text class="contact" x="815" y="193">Maple Ridge NJ 07190</text>
    <circle class="icon-disc" cx="1188" cy="172" r="16"/>
    <rect class="icon-stroke" x="1179" y="166" width="18" height="12"/>
    <path class="icon-stroke" d="M1179 166 L1188 173 L1197 166"/>
    <text class="contact" x="1218" y="179">dana@brightfoldpanels.example</text>
    <rect class="brand-square" x="760" y="318" width="52" height="52"/>
    <text class="brand-name" x="832" y="362">Brightfold Panel Works</text>
    <circle class="photo-ring" cx="1655" cy="300" r="155"/>
    <circle cx="1655" cy="300" r="150" fill="url(#room-tone)" role="img" aria-label="Photo of an office enclosed by glass partition walls"/>
    <text class="phone-line" x="1785" y="518" text-anchor="end">CALL US 973-555-0148</text>
    <text class="since" x="514" y="618">Since 1980</text>
    <circle class="icon-disc-dark" cx="785" cy="619" r="21"/>
    <circle class="icon-stroke-light" cx="785" cy="619" r="11"/>
    <path class="icon-stroke-light" d="M774 619 H796 M785 608 V630 M785 608 Q778 619 785 630 M785 608 Q792 619 785 630"/>
    <text class="web" x="826" y="620">brightfoldpanels.example</text>
  </g>

  <!-- Passenger-side view -->
  <g class="van van--passenger-side">
    <g transform="translate(2008 868) scale(-1 1)">
      <use href="#van-side"/>
    </g>
    <circle class="icon-disc" cx="530" cy="1031" r="16"/>
    <rect class="icon-stroke" x="521" y="1025" width="18" height="12"/>
    <path class="icon-stroke" d="M521 1025 L530 1032 L539 1025"/>
    <text class="contact" x="560" y="1042">dana@brightfoldpanels.example</text>
    <circle class="icon-disc" cx="991" cy="1040" r="16"/>
    <path class="icon-stroke" d="M991 1050 C985 1042 984 1038 984 1035 A7 7 0 0 1 998 1035 C998 1038 997 1042 991 1050 Z"/>
    <text class="contact" x="1023" y="1035">214 Alder Row</text>
    <text class="contact" x="1023" y="1056">Maple Ridge NJ 07190</text>
    <rect class="brand-square" x="560" y="1180" width="52" height="52"/>
    <text class="brand-name" x="632" y="1224">Brightfold Panel Works</text>
    <circle class="photo-ring" cx="345" cy="1165" r="160"/>
    <circle cx="345" cy="1165" r="155" fill="url(#room-tone)" role="img" aria-label="Photo of an open room divided by movable wall panels"/>
    <text class="phone-line" x="210" y="1382">CALL US 973-555-0148</text>
    <circle class="icon-disc-dark" cx="897" cy="1478" r="21"/>
    <circle class="icon-stroke-light" cx="897" cy="1478" r="11"/>
    <path class="icon-stroke-light" d="M886 1478 H908 M897 1467 V1489 M897 1467 Q890 1478 897 1489 M897 1467 Q904 1478 897 1489"/>
    <text class="web" x="938" y="1485">brightfoldpanels.example</text>
    <text class="since" x="1328" y="1482">Since 1980</text>
  </g>
</svg>
</body>
</html>
```